Plakat-Design für Pfandhaus gesucht
Zielgruppe
Wir sind ein Pfandhaus wir vergeben Pfandkredite gegen Wertgegenstände sowie Juwelier und Goldankauf aber in erster Linie steht das Pfandhaus .
Aufgabenstellung
Ich möchte gerne Plakate Buchen die an Straßen oder Hauswänden befestigt sind. Ca.3,5x3 Meter. Die Botschaft muss kurz und knapp sein da die Leute ja vorbeifahren.

```html
<!DOCTYPE html>
<html lang="de">
<head>
<meta charset="utf-8">
<title>Pfandhaus und Juwelier – Plakat</title>
<link href="https://fonts.googleapis.com/css2?family=Jost:wght@600;800&family=PT+Sans:wght@400;700&display=swap" rel="stylesheet">
<style>
  :root {
    --charcoal: #4a4a49;
    --white: #ffffff;
    --gold-light: #f6cd52;
    --gold-mid: #c9a745;
    --gold-bright: #ffd651;
    --gold-text: #d8b85a;
  }
  html, body {
    margin: 0;
    padding: 0;
    overflow: hidden;
    background: var(--charcoal);
  }
  .poster {
    position: relative;
    width: 1200px;
    height: 1029px;
    background: var(--charcoal);
    overflow: hidden;
  }
  .poster-graphics {
    position: absolute;
    inset: 0;
  }
  .headline {
    font-family: "Jost", "Futura", sans-serif;
    font-weight: 800;
    font-size: 182px;
    fill: var(--white);
    filter: drop-shadow(4px 5px 4px rgba(0,0,0,0.45));
  }
  .tagline {
    font-family: "Jost", "Futura", sans-serif;
    font-weight: 600;
    font-size: 46px;
    fill: var(--charcoal);
  }
  .tagline .tick {
    fill: var(--white);
    font-weight: 400;
  }
  .brand {
    position: absolute;
    left: 100px;
    top: 720px;
    width: 566px;
    text-align: center;
    font-family: "PT Sans", sans-serif;
    font-weight: 700;
    color: var(--gold-text);
    line-height: 1.1;
  }
  .brand-name {
    display: block;
    font-size: 56px;
    margin-top: 40px;
  }
  .brand-service {
    display: block;
    font-size: 56px;
    margin-top: 16px;
  }
  .contact {
    position: absolute;
    left: 728px;
    top: 738px;
    font-family: "PT Sans", sans-serif;
    color: var(--white);
  }
  .contact-address {
    margin: 0;
    font-weight: 700;
    font-size: 45px;
    line-height: 52px;
  }
  .contact-details {
    margin: 26px 0 0;
    font-weight: 400;
    font-size: 32px;
    line-height: 42px;
  }
</style>
</head>
<body>
<main class="poster">
  <svg class="poster-graphics" width="1200" height="1029" viewBox="0 0 1200 1029" aria-hidden="false">
    <defs>
      <linearGradient id="gold-band" x1="0" y1="0" x2="1" y2="0">
        <stop offset="0" stop-color="var(--gold-light)"/>
        <stop offset="0.5" stop-color="var(--gold-mid)"/>
        <stop offset="1" stop-color="var(--gold-bright)"/>
      </linearGradient>
    </defs>

    <polygon class="accent-stripe" points="0,123 1200,17 1200,39 0,140" fill="url(#gold-band)"/>
    <polygon class="claim-band" points="0,576 1200,472 1200,562 0,669" fill="url(#gold-band)"/>

    <g transform="rotate(-5 55 324)">
      <text class="headline" x="55" y="324" textLength="1103" lengthAdjust="spacingAndGlyphs">PFANDHAUS</text>
    </g>
    <g transform="rotate(-5 53 490)">
      <text class="headline" x="53" y="490" textLength="1108" lengthAdjust="spacingAndGlyphs">UND JUWELIER</text>
    </g>

    <g transform="rotate(-4.6 52 628)">
      <text class="tagline" x="52" y="628" textLength="1105" lengthAdjust="spacing"><tspan class="tick">✓</tspan> Technik  <tspan class="tick">✓</tspan> Gold  <tspan class="tick">✓</tspan> Silber  <tspan class="tick">✓</tspan> Hochwertiges Werkzeug</text>
    </g>
  </svg>

  <div class="brand">
    <span class="brand-name">Martin Weber</span>
    <span class="brand-service">Pfandkredit</span>
  </div>

  <address class="contact" style="font-style: normal;">
    <p class="contact-address">Lindenallee 14<br>66117 Saarbrücken</p>
    <p class="contact-details">Tel: 0681 - 12 345 678<br>www.pfandkredit-weber.de</p>
  </address>
</main>
</body>
</html>
```